Website Design for Business Law Firm

We have a logo and now we would like a web site design for our new website. Our small firm provides creative and aggressive transactional (not litigation) legal services to advise healthcare, technology, internet-based and traditional companies and investors in such companies on healthcare, technology, financing, mergers/acquisitions, real estate and other transactions, legal compliance and general corporate and business matters.

We would like to see a website design that is professional and appropriate for executives, professionals, investors and government regulators to visit, that conveys professionalism and competence while being a little edgy and modern - no typical legal motifs such as gavels, books, or scales of justice. We advise businesses and investors and guide them through complicated issues quickly, capably and differently from other law firms. We are part of the business team and get things done.

The logo is attached, and we like gray as a color to complement it. The intention of the logo is to convey that in a storm or challenging time, people come to this firm, and people come to this firm when they need the power and disruption to change things or shake them up.

I have also enclosed a picture of our business card for consideration.

On the other hand, you can check out the current simple site at www.venhollow.example to see we have used a space motif in the past to evoke that we help create stars (the nebula featured there). This is not a necessary part of the new website and it may look better without it.

We appreciate your creativity and look forward to designs.

Industry/Entity Type

Business

Requirements
Must have
• We anticipate the following pages, and you may submit different ideas for the different pages:
• 1. Landing page
• 2. Services pages - healthcare, IT/Technology, general counsel services, financings, mergers/acquisitions, mediation/arbitration, procurement and productization
• 3. About Us including contact information
• Our name and contact information:
• Quellane Law Firm, P.C.
• 8716 SW 19th Ave.
• Portland, OR 97213
• phone: 971.555.0143
• fax: 971.555.0187
Nice to have
• Please consider designs that enhance the impressions we are looking for
Should not have
• Please no gavels, scales of justice, law books, or similar traditional legal imagery.

```html
<!DOCTYPE html>
<html lang="en">
<head>
<meta charset="utf-8">
<title>Quellane Law Firm</title>
<link href="https://fonts.googleapis.com/css2?family=Noto+Sans:wght@400;700&family=Open+Sans:wght@400;600;700&display=swap" rel="stylesheet">
<style>
:root{
  --teal:#7fa4a7;
  --teal-dark:#5f8588;
  --navy:#2c3541;
  --charcoal:#2f2f2f;
  --page:#f6f6f6;
  --ink:#2b2b2b;
  --muted:#666;
  --line:#c9d6d7;
}
*{margin:0;padding:0;box-sizing:border-box}
html,body{width:967px;height:1200px;overflow:hidden}
body{font-family:"Noto Sans",sans-serif;color:var(--ink);background:var(--page);position:relative}
.abs{position:absolute}
.topbar{left:0;top:0;width:967px;height:18px;background:var(--navy);color:#dfe3e6;font-size:7.5px;line-height:18px}
.topbar .tagline{left:185px}
.topbar .mail{left:696px;display:flex;align-items:center;gap:5px;font-weight:700}
.header{left:0;top:18px;width:967px;height:79px;background:#f1f1f1}
.brand{left:185px;top:12px;width:238px;height:56px;background:#1e2329;display:flex;align-items:center;justify-content:center;gap:8px}
.brand-name{color:#fff;font-family:"Open Sans",sans-serif;font-size:26px;letter-spacing:6px;font-weight:400}
.brand-box{width:10px;height:10px;background:var(--teal)}
.social{display:flex;gap:6px}
.social span{width:20px;height:20px;border:1.5px solid var(--teal);display:block}
.header .social{left:704px;top:13px}
.phones{left:696px;top:40px;font-size:11px;color:#333;line-height:16px}
.phones div{display:flex;align-items:center;gap:5px}
.nav{left:0;top:97px;width:967px;height:27px;background:var(--teal)}
.nav ul{list-style:none;display:flex;position:absolute;left:195px;top:0;height:27px;align-items:center;gap:0}
.nav li{font-family:"Open Sans",sans-serif;font-size:9.5px;font-weight:600;color:#1f2a30;text-transform:uppercase;margin-right:39px}
.nav li.active{color:#fff}
.hero-bg{left:0;top:124px;width:967px;height:297px;background:#2f2f2f}
.hero{left:181px;top:124px;width:602px;height:297px;background:linear-gradient(120deg,#7b8590 0%,#d8d2cc 35%,#ece8e4 60%,#3c4b6a 100%)}
.hero-caption{left:181px;top:378px;width:602px;height:43px;background:rgba(235,235,235,.8)}
.hero-caption p{position:absolute;left:14px;top:9px;font-size:19px;color:#333}
.dots{right:16px;top:19px;display:flex;gap:5px}
.dots i{width:6px;height:6px;border-radius:50%;background:#777;display:block}
.dots i.on{background:#222}
.welcome-title{left:182px;top:446px;font-family:"Open Sans",sans-serif;font-size:23px;font-weight:700;color:var(--ink)}
.welcome-title span{color:var(--teal)}
.welcome-copy{left:183px;top:481px;width:395px;font-size:10.4px;line-height:14.5px;color:#555}
.welcome-copy p+p{margin-top:9px}
.profile{left:603px;top:447px;width:174px;height:174px;border-radius:50%;background:#fff;box-shadow:0 6px 8px rgba(0,0,0,.15);overflow:hidden}
.profile .photo{position:absolute;left:3px;top:3px;width:168px;height:168px;border-radius:50%;background:linear-gradient(180deg,#8b8a86 0%,#5a5852 55%,#2a2c30 100%);overflow:hidden}
.profile .name{position:absolute;left:0;top:122px;width:168px;height:46px;background:var(--teal);color:#fff;text-align:center}
.profile .name b{display:block;font-weight:400;font-size:15px;margin-top:4px}
.profile .name small{font-size:9px;font-weight:700}
.sec-head{font-family:"Open Sans",sans-serif;font-size:19px;font-weight:600;color:var(--ink);border-bottom:1.5px solid #bbb;height:27px}
.sec-head em{position:absolute;right:2px;top:6px;font-style:normal;font-size:11px;color:#555;font-weight:400}
.card{border:1px solid var(--line);background:#fff;font-size:8.5px;color:#666}
.services-card{left:181px;top:702px;width:295px;height:152px;padding:14px 15px}
.services-card h4{font-size:8.5px;color:#555;font-weight:700}
.services-card ul{list-style:none;columns:2;margin-top:9px;line-height:16.3px;padding-left:3px}
.services-card li::before{content:"";display:inline-block;width:4px;height:4px;border-radius:50%;background:var(--teal);margin-right:6px;vertical-align:middle}
.news-card{left:490px;top:702px;width:295px;height:152px;padding:12px 8px 0 12px}
.news-item{display:flex;gap:6px;padding:0 0 5px;border-bottom:1px dotted #ccc;margin-bottom:6px}
.news-item:last-child{border:none}
.news-item b.date{display:block;color:#555}
.news-item strong{color:#333}
.clients{left:0;top:882px;width:967px;height:168px;background:var(--teal)}
.clients h3{position:absolute;left:197px;top:16px;color:#fff;font-weight:400;font-size:17px}
.client{position:absolute;top:45px;width:97px;height:97px;border-radius:50%;background:#fff;border:2px solid #5c7a7d;display:flex;align-items:center;justify-content:center;font-size:17px;font-weight:700;color:#3c4b55}
.footer{left:0;top:1050px;width:967px;height:150px;background:var(--charcoal);color:#ddd;font-size:8.6px}
.footer h5{font-size:10px;font-weight:700;color:#fff;margin-bottom:9px}
.col{position:absolute;top:20px}
.links{list-style:none;columns:2;line-height:15.5px;width:160px}
.links li::before{content:"";display:inline-block;width:4px;height:4px;border-radius:50%;background:#888;margin-right:5px;vertical-align:middle}
.divider{position:absolute;top:20px;width:1px;height:105px;background:#444}
.email{width:141px;height:23px;background:#fff;border:1px solid #ccc;color:#999;font-size:8.5px;padding:5px 4px;margin-top:9px}
.submit{margin:7px 0 0 82px;width:60px;height:19px;background:var(--teal);color:#24363a;font-weight:700;font-size:9px;text-align:center;line-height:19px}
.contact-row{display:flex;gap:6px;align-items:flex-start;line-height:13.7px}
.contact-row svg{flex:none;margin-top:2px}
.copyright{left:190px;top:1175px;font-size:8.5px;color:#bbb}
.footer-rule{left:181px;top:1167px;width:605px;height:1px;background:#444}
.footer .social{position:absolute;left:716px;top:1172px}
.footer .social span{width:15px;height:15px;border:1px solid #999;background:#555}
</style>
</head>
<body>
<div class="abs topbar">
  <span class="abs tagline">Lorem ipsum dolor sit amet, consectetuer adipiscing elit, sed diam nonummy nibh.</span>
  <span class="abs mail"><svg width="11" height="8" viewBox="0 0 11 8"><rect x=".5" y=".5" width="10" height="7" fill="none" stroke="#ccc"/><path d="M.5 .5 5.5 4.5 10.5 .5" fill="none" stroke="#ccc"/></svg>info@quellane.example</span>
</div>

<header class="abs header">
  <div class="abs brand"><span class="brand-box"></span><span class="brand-name">QUELLANE</span></div>
  <div class="abs social"><span></span><span></span><span></span></div>
  <div class="abs phones">
    <div><svg width="11" height="11" viewBox="0 0 12 12"><circle cx="6" cy="6" r="5.3" fill="none" stroke="#999"/><path d="M4 3.5c0 3 2 4.8 4.5 4.8" stroke="#999" fill="none" stroke-width="1.5"/></svg>971.555.0162</div>
    <div><svg width="11" height="11" viewBox="0 0 12 12"><rect x="1" y="5" width="10" height="6" fill="#999"/><rect x="3" y="1" width="6" height="4" fill="none" stroke="#999"/></svg>971.555.0187</div>
  </div>
</header>

<nav class="abs nav"><ul>
  <li class="active">Home</li><li>Our Firm</li><li>Services</li><li>Case Studies</li><li>News Room</li><li>Resources</li><li>Contact</li>
</ul></nav>

<div class="abs hero-bg"></div>
<div class="abs hero" role="img" aria-label="Photo of three business people meeting around a document"></div>
<div class="abs hero-caption">
  <p>We Service For The Legal Business Industry</p>
  <div class="abs dots"><i></i><i></i><i></i><i class="on"></i></div>
</div>

<h1 class="abs welcome-title">WELCOME TO <span>QUELLANE</span></h1>
<div class="abs welcome-copy">
  <p>Lorem ipsum dolor sit amet, consectetuer adipiscing elit, sed diam nonummy nibh euismod tincidunt ut laoreet dolore magna aliquam erat volutpat. Ut wisi enim ad minim veniam, quis nostrud exerci tation ullamcorper suscipit lobortis nisl ut aliquip ex ea commodo consequat. Duis autem vel eum iriure dolor in hendrerit in vulputate velit esse molestie consequat, vel illum dolore eu feugiat nulla facili.</p>
  <p>Lorem ipsum dolor sit amet, consectetuer adipiscing elit, sed diam nonummy nibh eismod tincidunt ut laoreet dolore magna aliquam erat volutpat. Ut wisi enim ad minim veniam, quis nostrud exerci tation ullamcorper suscipit lobortis nisl ut aliquip laoreet dolore magna aliquam laoreet dolore magna aliquam.</p>
</div>
<div class="abs profile">
  <div class="photo" role="img" aria-label="Portrait of the firm's chief executive in a dark suit">
    <div class="name"><b>Mr. Owen Harlow</b><small>CEO</small></div>
  </div>
</div>

<h2 class="abs sec-head" style="left:181px;top:656px;width:295px">OUR SERVICES<em>view all ▸</em></h2>
<h2 class="abs sec-head" style="left:490px;top:656px;width:295px">LATEST NEWS<em>view all ▸</em></h2>

<div class="abs card services-card">
  <h4>Ytlaoreetd olore</h4>
  <p>Consectetuer adipiscing elit, sed diam nonu od tincidunt utlao reet dolore magna aliquam erat volutpat.</p>
  <ul>
    <li>Strategic Alliances</li><li>Real Estate</li><li>Business Relationships</li><li>Contracts</li><li>Outsourcing</li>
    <li>Procurements-Buying or Selling</li><li>Mergers and Acquisitions</li><li>Venture Formation &amp; Startup</li><li>Vendor Management</li><li>Venture Financing</li>
  </ul>
</div>

<div class="abs card news-card">
  <div class="news-item"><svg width="26" height="26" viewBox="0 0 26 26"><rect x="2" y="4" width="22" height="20" rx="2" fill="none" stroke="#bbb" stroke-width="1.5"/><path d="M7 2v5M19 2v5" stroke="#bbb" stroke-width="1.5"/><g fill="#ccc"><rect x="6" y="11" width="3" height="3"/><rect x="11.5" y="11" width="3" height="3"/><rect x="17" y="11" width="3" height="3"/><rect x="6" y="16" width="3" height="3"/><rect x="11.5" y="16" width="3" height="3"/><rect x="17" y="16" width="3" height="3"/></g></svg><div><b class="date">1 Dec, 2013</b>Consectetuer adipiscing elit, sed diam nonu od tincidunt utlao ree td olore magna aliquam erat volutpat <strong>and more.....</strong></div></div>
  <div class="news-item"><svg width="26" height="26" viewBox="0 0 26 26"><rect x="2" y="4" width="22" height="20" rx="2" fill="none" stroke="#bbb" stroke-width="1.5"/><path d="M7 2v5M19 2v5" stroke="#bbb" stroke-width="1.5"/><g fill="#ccc"><rect x="6" y="11" width="3" height="3"/><rect x="11.5" y="11" width="3" height="3"/><rect x="17" y="11" width="3" height="3"/><rect x="6" y="16" width="3" height="3"/><rect x="11.5" y="16" width="3" height="3"/><rect x="17" y="16" width="3" height="3"/></g></svg><div><b class="date">2 Dec, 2013</b>Consectetuer adipiscing elit, sed diam nonu od tincidunt utlao ree tdolore magna aliquam erat volutpat <strong>and more.....</strong></div></div>
  <div class="news-item"><svg width="26" height="26" viewBox="0 0 26 26"><rect x="2" y="4" width="22" height="20" rx="2" fill="none" stroke="#bbb" stroke-width="1.5"/><path d="M7 2v5M19 2v5" stroke="#bbb" stroke-width="1.5"/><g fill="#ccc"><rect x="6" y="11" width="3" height="3"/><rect x="11.5" y="11" width="3" height="3"/><rect x="17" y="11" width="3" height="3"/><rect x="6" y="16" width="3" height="3"/><rect x="11.5" y="16" width="3" height="3"/><rect x="17" y="16" width="3" height="3"/></g></svg><div><b class="date">3 Dec, 2013</b>Consectetuer adipiscing elit, sed diam nonu od tincidunt utlao reet dolore magna aliquam erat volutpat <strong>and more.....</strong></div></div>
</div>

<section class="abs clients">
  <h3>OUR CLIENTS</h3>
  <div class="client" style="left:190px">Solvane</div>
  <div class="client" style="left:311px">Mirazo</div>
  <div class="client" style="left:431px">Harvestline</div>
  <div class="client" style="left:552px">Kestrow</div>
  <div class="client" style="left:673px">Lorne</div>
</section>

<footer class="abs footer">
  <div class="col" style="left:190px"><h5>QUICK LINKS</h5>
    <ul class="links"><li>Home</li><li>Our Firm</li><li>Services</li><li>Case Studies</li><li>News Room</li><li>Resources</li><li>Contact</li></ul>
  </div>
  <div class="divider" style="left:365px"></div>
  <div class="col" style="left:393px"><h5>NEWS LETTERS</h5>
    <p>Get <b>FREE</b> News letters</p>
    <div class="email">Your Email</div>
    <div class="submit">SUBMIT</div>
  </div>
  <div class="divider" style="left:561px"></div>
  <div class="col" style="left:587px"><h5>CONTACT INFO</h5>
    <div class="contact-row"><svg width="8" height="10" viewBox="0 0 8 10"><path d="M4 10 1 5a3 3 0 1 1 6 0z" fill="#bbb"/></svg><span>Quellane Law Firm, P.C.<br>P.O. Box 7720, Portland, OR 97213</span></div>
    <div class="contact-row"><svg width="10" height="8" viewBox="0 0 10 8"><rect x=".5" y=".5" width="9" height="7" fill="none" stroke="#bbb"/><path d="M.5 .5 5 4 9.5 .5" fill="none" stroke="#bbb"/></svg><span>info@quellane.example</span></div>
    <div class="contact-row"><svg width="10" height="10" viewBox="0 0 10 10"><rect x="3" y=".5" width="4" height="9" rx="1" fill="none" stroke="#bbb"/></svg><span>971.555.0162</span></div>
    <div class="contact-row"><svg width="10" height="10" viewBox="0 0 10 10"><rect x=".5" y="4" width="9" height="5.5" fill="#bbb"/><rect x="2.5" y=".5" width="5" height="3.5" fill="none" stroke="#bbb"/></svg><span>971.555.0187</span></div>
  </div>
  <div class="social"><span></span><span></span><span></span></div>
</footer>
<div class="abs footer-rule"></div>
<div class="abs copyright">© 2013 QUELLANE. ALL RIGHTS RESERVED.</div>
</body>
</html>
```